Hand painted custom framed lithographs, poscard design

Pemberton and Voss is an high end interior design firm located in NY. We are proud to launch our custom framed, hand painted prints from Italy. We need a postcard for our Atlanta and Las Vegas trade show. Project should be printed by Jan 3rd. Feel free to use one or all images. You may also use any images from our website http://pembertonandvoss-example.com

Thank you in advance

Postcard will be double sided- put Expo/Trade show details on the backside of the card with the mailing label space.

Target Market(s)

Elegant Traditional

Industry/Entity Type

Trade

Font styles to use
Serif

Requirements
Must have
• Full Bleed Size (starting document size)
7.12" x 5.12"
181 x 130 mm
2135 x 1535 pixels
* Finished artwork should use the full bleed dimensions for best results.
Document Trim Size (final size after being cut)
7.00" x 5.00"
178 x 127 mm
2100 x 1500 pixels
* Please be sure to keep all text within the safe margin.
Resolution
300 DPI

Or

Full Bleed Size (starting document size)
6.12" x 4.12"
155 x 105 mm
1835 x 1235 pixels
6.00" x 4.00"
152 x 102 mm
1800 x 1200 pixels
Resolution
300 DPI
We are waiting on postage pricing

please try to use new uploaded background images. Copy: colors Chocolate gold white and Cream

Introducing

Our Custom framed hand colored lithographs, imported directly from Italy.

Reverse side of card
Please look for us at the:

Crestline National Gift and Home Interiors Fair
January 8-12, 2015
Building 4 - Floor 2, Booth K18
TradeHallPlex
Atlanta, GA

Desert Valley Furnishings/Interiors/Gift
January 18-22, 2015
Building F - Floor 3, Booth F3-0417
Grand Exhibit Pavilion
Las Vegas, NV
Nice to have
• Colors Chocolate, gold, white and cream logo feel free to improve on logo it looks a little ornate. We are looking for clean lines transitional (modern/traditonal)

```html
<!DOCTYPE html>
<html lang="en">
<head>
<meta charset="utf-8">
<title>Pemberton &amp; Voss Interiors – Trade Show Postcard</title>
<link href="https://fonts.googleapis.com/css2?family=Cinzel:wght@400;600&family=Cormorant+Garamond:wght@400;500;600&display=swap" rel="stylesheet">
<style>
  :root {
    --backdrop: #d9d3c8;
    --chocolate: #4a2c1a;
    --chocolate-deep: #3a2213;
    --gold: #c9a23f;
    --gold-light: #d9b75a;
    --cream: #f3ead6;
    --white: #ffffff;
    --ink: #3a2213;
    --photo-wall: #2a2233;
    --photo-warm: #8a5a32;
    --rule: #3a2213;
  }
  * { box-sizing: border-box; margin: 0; padding: 0; }
  html, body { width: 798px; height: 1200px; overflow: hidden; }
  body {
    position: relative;
    background: var(--backdrop);
    font-family: "Cormorant Garamond", Georgia, serif;
  }
  .card {
    position: absolute;
    left: 50px;
    width: 705px;
    background: var(--white);
    overflow: hidden;
  }
  .card--front { top: 42px; height: 546px; }
  .card--back { top: 614px; height: 544px; }
  .card-shapes { position: absolute; inset: 0; }

  /* Front */
  .brand-banner {
    position: absolute;
    left: 125px; top: 401px;
    width: 580px; height: 67px;
    background: var(--gold);
    display: flex; align-items: center; justify-content: center;
    font-size: 33px; font-weight: 500;
    letter-spacing: 1.5px;
    color: var(--ink);
  }

  /* Back – left panel */
  .about-banner {
    position: absolute;
    left: 50px; top: 41px;
    width: 250px; height: 52px;
    background: linear-gradient(90deg, var(--gold) 0%, var(--gold) 70%, var(--chocolate) 100%);
    box-shadow: 0 8px 8px -6px rgba(0,0,0,.45);
    display: flex; align-items: center; padding-left: 24px;
    font-family: "Cinzel", Georgia, serif;
    font-size: 31px;
    color: var(--ink);
  }
  .about-text {
    position: absolute;
    left: 30px; top: 112px;
    width: 330px;
    font-size: 16.5px;
    line-height: 23px;
    color: var(--cream);
  }
  .print-gallery { position: absolute; left: 18px; top: 262px; display: flex; gap: 8px; }
  .print-thumb {
    width: 130px; height: 94px;
    border-radius: 50%;
    border: 4px solid var(--gold);
  }
  .print-thumb--flower { background: radial-gradient(ellipse at center, #ece6d2 35%, #b34a36 75%); }
  .print-thumb--fish { background: radial-gradient(ellipse at center, #e3dccb 35%, #6a5236 80%); }
  .print-thumb--fruit { background: radial-gradient(ellipse at center, #e6e2d0 35%, #3f3326 80%); }

  .web-banner {
    position: absolute;
    left: 40px; top: 404px;
    width: 375px; height: 60px;
    background: var(--gold);
    box-shadow: 0 9px 9px -6px rgba(0,0,0,.45);
    display: flex; align-items: center; justify-content: center;
    font-size: 21px; font-weight: 500;
    color: var(--ink);
  }

  /* Back – right panel */
  .stamp-box {
    position: absolute;
    left: 603px; top: 40px;
    width: 60px; height: 71px;
    border: 1.5px solid var(--rule);
  }
  .show-details {
    position: absolute;
    left: 478px; top: 128px;
    width: 200px;
    color: var(--ink);
    font-size: 13px;
    line-height: 16px;
  }
  .show-details__intro {
    font-family: "Cinzel", Georgia, serif;
    font-size: 12.5px;
    font-weight: 600;
    color: var(--chocolate);
    border-bottom: 1px solid var(--gold);
    padding-bottom: 4px;
    margin-bottom: 8px;
  }
  .show {
    margin-bottom: 10px;
  }
  .show__name {
    font-weight: 600;
    color: var(--chocolate);
    overflow-wrap: anywhere;
  }
  .show__date { color: var(--gold); font-weight: 600; }

  .address-line {
    position: absolute;
    left: 495px; width: 168px;
    border-top: 1.5px solid var(--rule);
  }
  .address-line--1 { top: 432px; }
  .address-line--2 { top: 466px; }
  .address-line--3 { top: 500px; }
</style>
</head>
<body>

<section class="card card--front">
  <svg class="card-shapes" width="705" height="546" viewBox="0 0 705 546">
    <defs>
      <linearGradient id="roomGradient" x1="0" y1="0" x2="0" y2="1">
        <stop offset="0" stop-color="var(--photo-wall)"/>
        <stop offset="0.55" stop-color="#3a2e3a"/>
        <stop offset="0.8" stop-color="var(--photo-warm)"/>
        <stop offset="1" stop-color="#4a2c1a"/>
      </linearGradient>
    </defs>
    <rect width="705" height="546" fill="var(--chocolate)"/>
    <path d="M190,0 L705,0 L705,546 L330,546 C100,480 40,220 190,0 Z" fill="var(--white)"/>
    <path d="M270,0 L705,0 L705,515 C470,560 200,525 130,420 C75,300 115,130 270,0 Z" fill="var(--gold)"/>
    <path d="M320,0 L705,0 L705,500 C480,540 220,510 150,410 C100,310 140,140 320,0 Z" fill="url(#roomGradient)" role="img" aria-label="Photograph of a styled side table with a striped lamp, white hydrangeas, books, fruit, a clock and a framed botanical print"/>
  </svg>
  <div class="brand-banner">Pemberton &amp; Voss Interiors</div>
</section>

<section class="card card--back">
  <svg class="card-shapes" width="705" height="544" viewBox="0 0 705 544">
    <path d="M0,0 L290,0 C430,120 470,320 440,440 C410,520 150,535 0,535 Z" fill="var(--gold)"/>
    <path d="M0,0 L205,0 C380,110 440,300 420,420 C395,505 150,515 0,520 Z" fill="var(--chocolate)"/>
  </svg>

  <div class="about-banner">About Us</div>
  <p class="about-text">At Pemberton &amp; Voss Interiors we understand the process of creating a house that you want to come home to. Pemberton and Voss is an high end interior design firm located in NY. We are proud to launch our custom framed, hand painted prints from Italy.</p>

  <div class="print-gallery">
    <div class="print-thumb print-thumb--flower" role="img" aria-label="Framed hand painted botanical print of a red flower"></div>
    <div class="print-thumb print-thumb--fish" role="img" aria-label="Framed hand painted print of a pufferfish"></div>
    <div class="print-thumb print-thumb--fruit" role="img" aria-label="Framed hand painted print of a fruiting branch"></div>
  </div>

  <div class="web-banner">www.pembertonandvoss-example.com</div>

  <div class="stamp-box"></div>

  <div class="show-details">
    <p class="show-details__intro">Please look for us at the:</p>
    <div class="show">
      <p class="show__name">Crestline National Gift and Home Interiors Fair</p>
      <p class="show__date">January 8-12, 2015</p>
      <p>Building 4 - Floor 2, Booth K18</p>
      <p>TradeHallPlex</p>
      <p>Atlanta, GA</p>
    </div>
    <div class="show">
      <p class="show__name">Desert Valley Furnishings/ Interiors/Gift</p>
      <p class="show__date">January 18-22, 2015</p>
      <p>Building F - Floor 3, Booth F3-0417</p>
      <p>Grand Exhibit Pavilion</p>
      <p>Las Vegas, NV</p>
    </div>
  </div>

  <div class="address-line address-line--1"></div>
  <div class="address-line address-line--2"></div>
  <div class="address-line address-line--3"></div>
</section>

</body>
</html>
```